Business Card and Letterhead for Nurlo - modern real estate business

I need a double sided business card design for Nurlo. Please see business card brief here https://papers.trelvimo.net/sheet/q/7XrTbaLeZpMmQ2uWvd9HkCj4yNoEfsGi3lRtAz_pk/view?mode=shared

Please feel free to design the business cards however you feel best. I am happy to give some creative freedoms and then provide feedback from there.

Please then also create a letterhead to match the business card design

Colors

Designer to choose colors to be used in the design.

Requirements
Must have
• Must be a modern, elegant business card which looks very professional

```html
<!DOCTYPE html>
<html lang="en">
<head>
<meta charset="utf-8">
<title>Nurlo — Letterhead &amp; Business Cards</title>
<link rel="stylesheet" href="https://fonts.googleapis.com/css2?family=Exo+2:wght@400;600&display=swap">
<style>
  :root {
    --brand-red: #e01f26;
    --card-black: #1e1e1e;
    --paper: #ffffff;
    --stage: #ececec;
    --text-light: #f2f2f2;
    --rule-grey: #bdbdbd;
    --watermark: #fbeeee;
    --photo-top: #6f7f6a;
    --photo-bottom: #2a2a2c;
  }
  * { box-sizing: border-box; margin: 0; padding: 0; }
  html, body { width: 1200px; height: 1200px; overflow: hidden; }
  body {
    background: var(--stage);
    font-family: "Exo 2", sans-serif;
    position: relative;
  }
  .brand-name {
    font-family: "Exo 2", sans-serif;
    font-weight: 600;
    color: var(--brand-red);
    letter-spacing: 0.04em;
    line-height: 1;
    white-space: nowrap;
  }

  /* Letterhead */
  .letterhead {
    position: absolute;
    left: 266px; top: 168px;
    width: 668px; height: 864px;
    background: var(--paper);
    overflow: hidden;
  }
  .letterhead__header {
    position: absolute; left: 0; right: 0; top: 0; height: 102px;
  }
  .letterhead__rule {
    position: absolute; top: 101px; height: 1px; background: var(--rule-grey);
  }
  .letterhead__rule--left { left: 0; width: 196px; }
  .letterhead__rule--right { right: 0; width: 204px; }
  .letterhead__logo {
    position: absolute; left: 0; right: 0; top: 54px;
    text-align: center; font-size: 60px;
  }
  .letterhead__watermark {
    position: absolute; left: 26px; top: 716px;
    font-size: 118px; color: var(--watermark);
  }
  .letterhead__footer {
    position: absolute; left: 0; right: 0; bottom: 0; height: 69px;
    background: var(--card-black);
    border-top: 2px solid var(--brand-red);
    color: var(--text-light);
    text-align: center;
  }
  .letterhead__address {
    display: inline-block; margin-top: 9px; padding: 0 30px 4px;
    font-size: 12px; letter-spacing: 0.04em;
    border-bottom: 1px solid #555;
  }
  .letterhead__contacts {
    display: flex; justify-content: center; gap: 12px;
    margin-top: 7px; font-size: 12.5px; letter-spacing: 0.05em;
  }
  .contact-item { display: inline-flex; align-items: center; gap: 5px; }
  .contact-item svg { width: 10px; height: 10px; fill: var(--brand-red); }

  /* Business cards */
  .business-card {
    position: absolute; background: var(--card-black); color: var(--text-light);
  }
  .business-card--front {
    left: 48px; top: 243px; width: 210px; height: 340px; text-align: center;
  }
  .business-card--back {
    left: 279px; top: 373px; width: 340px; height: 210px;
    display: flex; align-items: center; justify-content: center;
  }
  .business-card--back .brand-name { font-size: 64px; }
  .card__logo { position: absolute; left: 0; right: 0; top: 34px; font-size: 22px; }
  .card__photo {
    position: absolute; left: 58px; top: 83px; width: 94px; height: 103px;
    border: 3px solid var(--paper); outline: 1.5px solid var(--brand-red);
    background: linear-gradient(180deg, var(--photo-top), var(--photo-bottom));
  }
  .card__name {
    position: absolute; left: 0; right: 0; top: 211px;
    font-size: 14px; font-weight: 600; color: var(--brand-red); letter-spacing: 0.05em;
  }
  .card__title {
    position: absolute; left: 0; right: 0; top: 227px; font-size: 8px; letter-spacing: 0.06em;
  }
  .card__icon-row {
    position: absolute; left: 20px; right: 20px; top: 243px;
    display: flex; align-items: center; justify-content: center; gap: 3px;
  }
  .card__icon-row .rule { flex: 1; height: 1px; background: #666; margin: 0 3px; }
  .icon-dot {
    width: 10px; height: 10px; border-radius: 50%; background: var(--brand-red);
    display: inline-flex; align-items: center; justify-content: center;
  }
  .icon-dot svg { width: 6px; height: 6px; fill: var(--paper); }
  .card__details {
    position: absolute; left: 0; right: 0; top: 259px;
    font-size: 8px; line-height: 10.4px; letter-spacing: 0.05em;
  }
  .card__divider {
    position: absolute; left: 30px; right: 30px; top: 297px; height: 1px; background: #555;
  }
  .card__address {
    position: absolute; left: 0; right: 0; top: 303px; font-size: 8px; letter-spacing: 0.04em;
  }
</style>
</head>
<body>
<svg width="0" height="0" style="position:absolute">
  <defs>
    <symbol id="icon-phone" viewBox="0 0 24 24"><path d="M6.6 10.8a15.1 15.1 0 0 0 6.6 6.6l2.2-2.2a1 1 0 0 1 1-.25 11.4 11.4 0 0 0 3.6.57 1 1 0 0 1 1 1V20a1 1 0 0 1-1 1A17 17 0 0 1 3 4a1 1 0 0 1 1-1h3.5a1 1 0 0 1 1 1c0 1.25.2 2.45.57 3.57a1 1 0 0 1-.25 1z"/></symbol>
    <symbol id="icon-mail" viewBox="0 0 24 24"><path d="M2 5h20v14H2zm2 2v.5l8 5 8-5V7zm0 3v7h16v-7l-8 5z"/></symbol>
    <symbol id="icon-globe" viewBox="0 0 24 24"><path d="M12 2a10 10 0 1 0 0 20 10 10 0 0 0 0-20zm6.9 6h-3a15 15 0 0 0-1.3-4A8 8 0 0 1 18.9 8zM12 4c.8 1.1 1.5 2.5 1.9 4h-3.8c.4-1.5 1.1-2.9 1.9-4zM4.3 14a8 8 0 0 1 0-4h3.4a16 16 0 0 0 0 4zm.8 2h3a15 15 0 0 0 1.3 4A8 8 0 0 1 5.1 16zm3-8h-3a8 8 0 0 1 4.3-4 15 15 0 0 0-1.3 4zM12 20c-.8-1.1-1.5-2.5-1.9-4h3.8c-.4 1.5-1.1 2.9-1.9 4zm2.3-6H9.7a14 14 0 0 1 0-4h4.6a14 14 0 0 1 0 4zm.3 6a15 15 0 0 0 1.3-4h3a8 8 0 0 1-4.3 4zm1.7-6a16 16 0 0 0 0-4h3.4a8 8 0 0 1 0 4z"/></symbol>
  </defs>
</svg>

<main class="letterhead">
  <header class="letterhead__header">
    <span class="letterhead__rule letterhead__rule--left"></span>
    <div class="letterhead__logo brand-name">NURLO</div>
    <span class="letterhead__rule letterhead__rule--right"></span>
  </header>

  <section class="business-card business-card--front">
    <div class="card__logo brand-name">NURLO</div>
    <div class="card__photo" role="img" aria-label="Portrait photo of the agent outdoors"></div>
    <div class="card__name">REID CALLOWAY</div>
    <div class="card__title">Licenced Real Estate Agent</div>
    <div class="card__icon-row">
      <span class="rule"></span>
      <span class="icon-dot"><svg><use href="#icon-phone"/></svg></span>
      <span class="icon-dot"><svg><use href="#icon-mail"/></svg></span>
      <span class="icon-dot"><svg><use href="#icon-globe"/></svg></span>
      <span class="rule"></span>
    </div>
    <div class="card__details">
      0491 570 156 | 1300 975 310<br>
      Reid@nurlo.com<br>
      www.nurlo.com
    </div>
    <div class="card__divider"></div>
    <div class="card__address">PO Box 3172, Tallowood NSW 2790</div>
  </section>

  <section class="business-card business-card--back">
    <div class="brand-name">NURLO</div>
  </section>

  <div class="letterhead__watermark brand-name" aria-hidden="true">NURLO</div>

  <footer class="letterhead__footer">
    <div class="letterhead__address">PO Box 3172, Tallowood NSW 2790</div>
    <div class="letterhead__contacts">
      <span class="contact-item"><svg><use href="#icon-phone"/></svg>0491 570 156</span>
      <span class="contact-item"><svg><use href="#icon-phone"/></svg>1300 975 310</span>
      <span class="contact-item"><svg><use href="#icon-mail"/></svg>Reid@nurlo.com</span>
      <span class="contact-item"><svg><use href="#icon-globe"/></svg>www.nurlo.com</span>
    </div>
  </footer>
</main>
</body>
</html>
```